Consulting Company Business Card

I am looking for a minimalist, classy, professional design on my business card. I would like it to be double-sided. I want to use the font and color scheme of my logo which are attached. Please be creative in the designs that you send me. I want to play off the design of my logo with the inner C that is Green and Blue broken up with the white.
Target Market(s)
Small Businesses
Industry/Entity Type
Consulting
Contact Information for Business Card
Dale M. Whitcombe, CPA CGMA, 555-014-2873, dwhitcombe@vorantaadvisory.example, www.vorantaadvisory.example

```html
<!DOCTYPE html>
<html lang="en">
<head>
<meta charset="utf-8">
<title>Voranta Advisory – Business Card</title>
<link href="https://fonts.googleapis.com/css2?family=Montserrat:wght@400;500;700&display=swap" rel="stylesheet">
<style>
  :root {
    --navy: #1a2d4e;
    --navy-deep: #14264a;
    --ink: #1f3050;
    --teal: #1e8c87;
    --paper: #f7f7f7;
    --backdrop: #c9c6c3;
  }
  * { margin: 0; padding: 0; box-sizing: border-box; }
  html, body {
    width: 1200px; height: 1200px; overflow: hidden;
    background: var(--backdrop);
    font-family: "Montserrat", sans-serif;
  }
  .card {
    position: absolute; left: 243px; width: 702px; height: 400px;
    border-radius: 20px;
  }
  .card-front {
    top: 170px;
    background: linear-gradient(135deg, var(--navy) 0%, var(--navy-deep) 100%);
  }
  .front-brand {
    position: absolute; left: 64px; top: 278px;
    display: flex; align-items: center; gap: 12px;
    color: #ffffff; font-weight: 700; font-size: 20px; letter-spacing: 1px;
  }
  .brand-dot {
    width: 30px; height: 30px; border-radius: 50%;
  }
  .front-brand .brand-dot { background: #ffffff; }
  .card-back {
    top: 630px;
    background: linear-gradient(160deg, #fbfbfb 0%, var(--paper) 50%, #e2e2e2 100%);
  }
  .back-brand {
    position: absolute; left: 40px; top: 150px; width: 292px;
    display: flex; flex-direction: column; align-items: center; gap: 12px;
    color: var(--ink); font-weight: 700; font-size: 26px; letter-spacing: 0.5px;
    text-align: center; line-height: 1.1;
  }
  .back-brand .brand-dot { width: 56px; height: 56px; background: var(--ink); }
  .divider {
    position: absolute; left: 352px; top: 128px; width: 2px; height: 144px;
    background: var(--ink);
  }
  .contact {
    position: absolute; left: 367px; top: 126px; color: var(--ink);
  }
  .contact-name { font-weight: 700; font-size: 21px; letter-spacing: 0.5px; text-transform: uppercase; }
  .contact-title { font-weight: 500; font-size: 16px; letter-spacing: 1px; margin-top: 0px; }
  .contact-lines { margin-top: 32px; font-size: 16.5px; line-height: 25px; font-weight: 500; }
</style>
</head>
<body>
  <section class="card card-front">
    <div class="front-brand"><span class="brand-dot"></span>VORANTA ADVISORY</div>
  </section>

  <section class="card card-back">
    <div class="back-brand"><span class="brand-dot"></span>VORANTA ADVISORY</div>
    <div class="divider"></div>
    <div class="contact">
      <div class="contact-name">Dale M. Whitcombe</div>
      <div class="contact-title">CPA CGMA</div>
      <div class="contact-lines">
        <div>555 · 014 · 2873</div>
        <div>dwhitcombe@vorantaadvisory.example</div>
        <div>www.vorantaadvisory.example</div>
      </div>
    </div>
  </section>
</body>
</html>
```